Business Card Design

Hi I need a business card designed, we already have the business name logo artwork and would like some concept ideas for the Bus Card layout.
On the back of the card i want to include the products and services that we offer.
We are a Plastics Sheeting manufacture based in Perth Australia.

                                       

We need a BC design for a company called Tarnby Plastics based in Perth Australia.

We supply from DIY to Trade & Industrial  Engineering Markets.

We specialise in:

·         Cut to size panels  (all shapes and sizes)

·         Plastics fabrication & Welding

·         Custom Designs

·         Plastic Repairs

·         PVC Pipe Slotting & PVC Pipe Threading

·         Supplier of all types of engineering plastics and profiles.

Including:           Acrylic / Vendrix

                               Polycarbonate / Moravite

                               Prismatic Light Diffuser

                               Tubrasin

                               HDPE / UHMWPE

                               PVC / PVC Foam

                               Nylon

                               HIPS

```html
<!DOCTYPE html>
<html lang="en">
<head>
<meta charset="utf-8">
<title>Tarnby Plastics – Business Card</title>
<link rel="stylesheet" href="https://fonts.googleapis.com/css2?family=Open+Sans:wght@400;600;700&display=swap">
<style>
  :root {
    --bg: #2a2a2c;
    --navy: #0f2a5c;
    --navy-deep: #0c2554;
    --red: #a3132b;
    --paper: #f7f7f7;
    --back-text: #4f8fc9;
  }
  * { box-sizing: border-box; margin: 0; padding: 0; }
  html, body { width: 1200px; height: 900px; overflow: hidden; }
  body {
    background: var(--bg);
    font-family: "Open Sans", Arial, sans-serif;
    display: flex;
    align-items: center;
    justify-content: center;
    gap: 40px;
  }
  .card {
    position: relative;
    width: 540px;
    height: 330px;
    border-radius: 22px;
    overflow: hidden;
  }
  /* Back face */
  .card--back {
    background: var(--navy-deep);
    display: flex;
    flex-direction: column;
    align-items: center;
    justify-content: center;
    gap: 18px;
  }
  .brand {
    display: flex;
    align-items: center;
    gap: 10px;
    font-weight: 700;
    line-height: 1;
  }
  .brand__square { width: 16px; height: 16px; }
  .card--back .brand { color: #fff; font-size: 40px; }
  .card--back .brand__square { background: #fff; }
  .services {
    list-style: none;
    text-align: center;
    color: var(--back-text);
    font-size: 14px;
    line-height: 1.55;
  }
  /* Front face */
  .card--front { background: var(--paper); color: var(--navy); }
  .card--front .brand {
    position: absolute; left: 30px; top: 42px;
    color: var(--navy); font-size: 34px;
  }
  .card--front .brand__square { background: var(--navy); }
  .legal {
    position: absolute; right: 28px; top: 24px;
    font-size: 8px; line-height: 1.3; font-weight: 600;
  }
  .person { position: absolute; left: 34px; top: 140px; }
  .person__name { color: var(--red); font-size: 20px; font-weight: 400; }
  .person__role { font-size: 13px; }
  .contacts {
    position: absolute; left: 34px; top: 196px;
    list-style: none; font-size: 14.5px; line-height: 1.45;
  }
  .contacts__label { display: inline-block; width: 18px; color: var(--red); }
  .address {
    position: absolute; left: 320px; top: 124px;
    font-style: normal; font-size: 13.5px; line-height: 1.4;
  }
  .base-band {
    position: absolute; left: 0; right: 0; bottom: 0;
    height: 22px;
    background: var(--navy);
    border-top: 4px solid var(--red);
  }
</style>
</head>
<body>
  <section class="card card--back" aria-label="Card back">
    <div class="brand"><span class="brand__square"></span>Tarnby Plastics</div>
    <ul class="services">
      <li>Industrial Products • Engineering Products</li>
      <li>Signage Products • Building Products</li>
      <li>Storage Systems • Display Materials</li>
    </ul>
  </section>

  <section class="card card--front" aria-label="Card front">
    <div class="brand"><span class="brand__square"></span>Tarnby Plastics</div>
    <p class="legal">Kellmore Holdings Pty Ltd<br>T/A Tarnby Plastics ABN: TBA</p>
    <div class="person">
      <h1 class="person__name">Daniel Hartwell</h1>
      <p class="person__role">managing director</p>
    </div>
    <ul class="contacts">
      <li><span class="contacts__label">M</span>0400 318 227</li>
      <li><span class="contacts__label">P</span>08 9471 3308</li>
      <li><span class="contacts__label">F</span>08 9471 3309</li>
      <li><span class="contacts__label">E</span>sales@tarnbyplastics.com.au</li>
    </ul>
    <address class="address">
      Unit 4/18 Brindle Circuit<br>
      Larkdale WA 6158<br>
      PO Box 2275 Larkdale<br>
      DC WA 6972
    </address>
    <div class="base-band"></div>
  </section>
</body>
</html>
```